Corvana Wound Care Business card design

We need a business card designed around our logo which was provided. The logo of preference is the colored. Also the colors and fonts were provided.

Target Market(s)

Our Referral partners are home health agencies.

Industry/Entity Type

Healthcare

Contact Information for Business Card

Name , Phone #, Email , Title

Requirements
Nice to have
• Creativity
Should not have
• basic

```html
<!DOCTYPE html>
<html lang="en">
<head>
<meta charset="utf-8">
<title>Corvana Wound Care – Business Card</title>
<link href="https://fonts.googleapis.com/css2?family=Lora:wght@500;600&family=Montserrat:wght@500;600&display=swap" rel="stylesheet">
<style>
  :root {
    --navy: #033b85;
    --navy-deep: #06418d;
    --indigo: #283c92;
    --sky: #2299dd;
    --sky-soft: #3aa3e3;
    --paper: #ffffff;
    --ink: #0b3b84;
  }
  * { margin: 0; padding: 0; box-sizing: border-box; }
  html, body { width: 873px; height: 1200px; overflow: hidden; background: var(--paper); }
  .canvas { position: relative; width: 873px; height: 1200px; }

  .card { position: absolute; left: 218px; width: 435px; height: 249px; overflow: hidden; }
  .card--front { top: 333px; background: var(--paper); border: 0.6px solid #555; }
  .card--back { top: 616px; background: var(--navy); }

  .front-art { position: absolute; inset: 0; }

  .brand { position: absolute; display: flex; align-items: center; gap: 8px;
    font-family: "Lora", Georgia, serif; font-weight: 600; white-space: nowrap; }
  .brand__dot { border-radius: 50%; flex: none; }
  .brand--front { left: 23px; top: 40px; font-size: 23px; color: var(--ink); }
  .brand--front .brand__dot { width: 16px; height: 16px; background: var(--sky); }

  .person__name { position: absolute; left: 24px; top: 103px; font-family: "Lora", Georgia, serif;
    font-weight: 500; font-size: 21px; color: var(--ink); }
  .person__title { position: absolute; left: 25px; top: 131px; font-family: "Montserrat", Arial, sans-serif;
    font-weight: 600; font-size: 9px; letter-spacing: 2.2px; color: var(--sky); }
  .person__rule { position: absolute; left: 25px; top: 148px; width: 141px; height: 1px; background: var(--sky); }

  .contact { position: absolute; left: 25px; top: 158px; list-style: none; }
  .contact__row { display: flex; align-items: center; height: 17.5px; font-family: "Lora", Georgia, serif;
    font-size: 9px; color: var(--ink); }
  .contact__icon { width: 13px; height: 13px; margin-right: 6px; flex: none; }

  .tagline-band { position: absolute; left: 0; bottom: 0; width: 435px; height: 29px;
    background: linear-gradient(90deg, var(--indigo) 0%, #2a62b2 40%, #1b8ad6 70%, var(--navy-deep) 88%); 
    display: flex; align-items: center; }
  .tagline-band__dot { position: absolute; left: 29px; top: 11px; width: 8px; height: 8px; border-radius: 50%; background: var(--paper); }
  .tagline-band__divider { position: absolute; left: 55px; top: 8px; width: 0.6px; height: 12px; background: rgba(255,255,255,.6); }
  .tagline-band__text { position: absolute; left: 67px; font-family: "Montserrat", Arial, sans-serif; font-weight: 500;
    font-size: 6.6px; letter-spacing: 0.8px; color: var(--paper); }

  .brand--back { left: 0; right: 0; top: 92px; justify-content: center; font-size: 28px; color: var(--paper); }
  .brand--back .brand__dot { width: 18px; height: 18px; background: var(--sky); }

  .back-divider { position: absolute; top: 201px; height: 1px; width: 92px; background: var(--sky); }
  .back-divider--left { left: 115px; }
  .back-divider--right { left: 228px; }
  .back-divider__dot { position: absolute; left: 214px; top: 198px; width: 7px; height: 7px; border-radius: 50%; background: var(--sky); }
  .back-url { position: absolute; left: 0; right: 0; top: 211px; text-align: center; font-family: "Montserrat", Arial, sans-serif;
    font-weight: 500; font-size: 9px; letter-spacing: 2px; color: var(--paper); }
</style>
</head>
<body>
<main class="canvas">
  <section class="card card--front" aria-label="Business card front">
    <svg class="front-art" viewBox="0 0 435 249" width="435" height="249" aria-hidden="true">
      <path d="M373 0 L435 0 L435 249 L248 249 L257 220 C318 162 362 100 373 0 Z" fill="#06418d"/>
      <path d="M353 0 L373 0 C362 100 318 162 257 220 L250 223 C305 168 343 108 353 0 Z" fill="#2a9be0"/>
    </svg>

    <div class="brand brand--front"><span class="brand__dot"></span>Corvana Wound Care</div>

    <h1 class="person__name">Name Here</h1>
    <p class="person__title">TITLE HERE</p>
    <div class="person__rule"></div>

    <ul class="contact">
      <li class="contact__row">
        <svg class="contact__icon" viewBox="0 0 14 14"><circle cx="7" cy="7" r="7" fill="#0b3b84"/><path d="M4.6 3.6c.4-.3.8-.2 1 .2l.6 1.2c.1.3 0 .6-.2.8l-.4.4c.4.9 1.1 1.6 2 2l.4-.4c.2-.2.5-.3.8-.2l1.2.6c.4.2.5.6.2 1l-.5.6c-.4.4-1 .5-1.6.2-1.8-.8-3.1-2.1-3.9-3.9-.2-.6-.1-1.2.3-1.6z" fill="#fff"/></svg>
        (123) 456-7890
      </li>
      <li class="contact__row">
        <svg class="contact__icon" viewBox="0 0 14 14"><circle cx="7" cy="7" r="7" fill="#0b3b84"/><rect x="3.8" y="4.8" width="6.4" height="4.4" fill="none" stroke="#fff" stroke-width=".8"/><path d="M3.8 4.8 L7 7.4 L10.2 4.8 M3.8 9.2 L6 7 M10.2 9.2 L8 7" fill="none" stroke="#fff" stroke-width=".7"/></svg>
        name@email.com
      </li>
      <li class="contact__row">
        <svg class="contact__icon" viewBox="0 0 14 14"><circle cx="7" cy="7" r="7" fill="#0b3b84"/><g fill="none" stroke="#fff" stroke-width=".6"><circle cx="7" cy="7" r="3.4"/><ellipse cx="7" cy="7" rx="1.5" ry="3.4"/><path d="M3.6 7h6.8M4.1 5.3h5.8M4.1 8.7h5.8"/></g></svg>
        www.corvanawoundcare.com
      </li>
    </ul>

    <footer class="tagline-band">
      <span class="tagline-band__dot"></span>
      <span class="tagline-band__divider"></span>
      <span class="tagline-band__text">PARTNERING FOR BETTER PATIENT OUTCOMES</span>
    </footer>
  </section>

  <section class="card card--back" aria-label="Business card back">
    <div class="brand brand--back"><span class="brand__dot"></span>Corvana Wound Care</div>
    <span class="back-divider back-divider--left"></span>
    <span class="back-divider__dot"></span>
    <span class="back-divider back-divider--right"></span>
    <p class="back-url">www.corvanawoundcare.com</p>
  </section>
</main>
</body>
</html>
```